Personal Brand Business Card

I am looking for a design that I will use as my personal brand that conveys class (think 1920s gentlemen) and is timeless. I will be putting this on a pearl white, letter pressed, cotton business card.  I’m thinking maybe something with my initials on the front they will flip over for the rest of my information.  But don’t let that limit you.
The information I will have on the back of the business card will be my name, email, and phone number.
Some of the attributes that best describe me are: loyal, dependable, creative, risk taker, open minded, competitive, and empathetic.  I can adapt to my environment quickly and can get along with anyone.  I get excited by figuring out the way things work and finding solutions to problems.

Industry/Entity Type
Business

```html
<!DOCTYPE html>
<html lang="en">
<head>
<meta charset="utf-8">
<title>Graham Whitlock — Business Card</title>
<link rel="stylesheet" href="https://fonts.googleapis.com/css2?family=Libre+Baskerville:wght@400;700&display=swap">
<style>
  :root {
    --backdrop: #9b5e60;
    --card: #ececec;
    --ink-red: #861719;
    --ink-dark: #3a3a3a;
    --shadow: rgba(60, 20, 22, 0.35);
  }
  * { box-sizing: border-box; margin: 0; padding: 0; }
  html, body {
    width: 1200px;
    height: 900px;
    overflow: hidden;
    background: var(--backdrop);
    font-family: "Libre Baskerville", Georgia, serif;
  }
  .canvas {
    position: relative;
    width: 1200px;
    height: 900px;
  }
  .card {
    position: absolute;
    top: 170px;
    width: 330px;
    height: 560px;
    background: var(--card);
    border-radius: 16px;
    box-shadow: 0 6px 18px var(--shadow);
  }
  .card--notes { left: 230px; }
  .card--contact { left: 640px; }

  /* Notes side */
  .notes-lines {
    list-style: none;
    position: absolute;
    top: 34px;
    left: 34px;
    right: 34px;
  }
  .notes-lines li {
    height: 17px;
    border-bottom: 2px dotted var(--ink-dark);
  }
  .notes-lines li:nth-child(even) { border-bottom-color: var(--ink-red); }
  .notes-mark {
    position: absolute;
    left: 34px;
    bottom: 40px;
    font-size: 34px;
    font-weight: 700;
    color: var(--ink-red);
    opacity: 0.85;
  }

  /* Contact side */
  .contact-mark {
    position: absolute;
    top: 170px;
    left: 0;
    right: 0;
    text-align: center;
    font-size: 50px;
    font-weight: 700;
    color: var(--ink-red);
    letter-spacing: -1px;
  }
  .contact-details {
    position: absolute;
    top: 300px;
    left: 30px;
    right: 30px;
    text-align: center;
    color: var(--ink-red);
  }
  .contact-name {
    font-size: 19px;
    font-weight: 700;
    letter-spacing: 1.5px;
    text-transform: uppercase;
    padding-bottom: 6px;
    border-bottom: 1.5px solid var(--ink-red);
  }
  .contact-phone {
    font-size: 14px;
    font-weight: 700;
    margin-top: 6px;
    padding-bottom: 4px;
    border-bottom: 1.5px solid var(--ink-red);
  }
  .contact-email {
    font-size: 14px;
    font-weight: 700;
    margin-top: 4px;
  }
</style>
</head>
<body>
<main class="canvas">
  <section class="card card--notes" aria-label="Card back with note lines">
    <ul class="notes-lines">
      <li></li><li></li><li></li><li></li><li></li><li></li><li></li>
      <li></li><li></li><li></li><li></li><li></li><li></li><li></li>
      <li></li><li></li><li></li><li></li><li></li><li></li><li></li>
      <li></li><li></li>
    </ul>
    <div class="notes-mark">Whitlock</div>
  </section>

  <section class="card card--contact" aria-label="Card front with contact details">
    <div class="contact-mark">Whitlock</div>
    <div class="contact-details">
      <p class="contact-name">Graham Whitlock</p>
      <p class="contact-phone">215-555-0182</p>
      <p class="contact-email">graham.whitlock@mail.com</p>
    </div>
  </section>
</main>
</body>
</html>
```